Legislative compliance to home owners, landlords and agents

Logo, business card and stationaly header for a sole trader offering sevices in the UK to home owners, landlords and Letting agents to meet legislation requirement relating to sale and leasing of rental domestic homes. Services offered include Legionella Risk Assessment, Portable Appliance Testing and Energy Performance Certificates. Logo to include depiction of a house and compliance tick list images. Have an existing card with water splash image to reflect water testing, so considering picking up same wave blue. Company name Talvane Property Services. Web www.talvaneps-example.com. email: info@talvaneps-example.com. Address: Glenmorrow, Aberdeen. All three services to be listed. Name as existing card.,

Target Market(s)

UK home owners, landlords, lettings and estate agents

Industry/Entity Type

Property Management

Contact Information for Business Card

Derek Hollingsby CEng, MSoHTF
Address: Glenmorrow, Aberdeen
Web: www.talvaneps-example.com
e-mail info@talvaneps-example.com
Phone: 07921 458 302
Services: Legionella Risk Assessment, Portable Appliance Testing, Energy Performance Certificate

Logo Text

Talvane Property Services

Font styles to use
Sans Serif

Colors

Designer to choose colors to be used in the design.

Requirements
Must have
• Suitable for standard UK business card size 85 mm x 55 mm, with allowance for safety border/ bleed such that colours extend to outside border of card once printed
Nice to have
• Clear font style and layout
• Happy to see images depicting phone, address etc

```html
<!DOCTYPE html>
<html lang="en">
<head>
<meta charset="utf-8">
<title>Talvane Property Services – Business Card</title>
<link href="https://fonts.googleapis.com/css2?family=Open+Sans:ital,wght@0,400;0,600;0,700;1,400&display=swap" rel="stylesheet">
<style>
  :root {
    --page-bg: #ecebe8;
    --card-bg: #ffffff;
    --card-shade: #f0f0f1;
    --card-shade-deep: #e9e9eb;
    --navy: #2a2d78;
    --text-grey: #7d7d82;
    --rule-grey: #b9b9c0;
    --ink: #333340;
  }
  html, body {
    margin: 0;
    width: 1200px;
    height: 1200px;
    overflow: hidden;
    background: var(--page-bg);
    font-family: "Open Sans", Arial, sans-serif;
  }
  .canvas {
    width: 1200px;
    height: 1200px;
    display: flex;
    align-items: center;
    justify-content: center;
  }
  .business-card {
    position: relative;
    width: 1000px;
    height: 647px;
    background: var(--card-bg);
    box-shadow: 0 10px 30px rgba(0,0,0,0.12);
    overflow: hidden;
  }
  .card-shading {
    position: absolute;
    inset: 0;
    width: 1000px;
    height: 647px;
  }
  .brand {
    position: absolute;
    left: 90px;
    top: 372px;
    display: flex;
    align-items: center;
    gap: 14px;
  }
  .brand-mark {
    width: 22px;
    height: 22px;
    background: var(--navy);
  }
  .brand-name {
    font-size: 32px;
    font-weight: 700;
    color: var(--navy);
    white-space: nowrap;
  }
  .holder {
    position: absolute;
    left: 150px;
    top: 232px;
    width: 430px;
    text-align: right;
  }
  .holder-name {
    font-size: 36px;
    font-weight: 700;
    color: var(--navy);
    letter-spacing: 1px;
    margin: 0;
    line-height: 1.1;
    white-space: nowrap;
  }
  .holder-title {
    font-size: 22px;
    color: var(--text-grey);
    margin: 8px 0 0;
  }
  .divider {
    position: absolute;
    left: 610px;
    top: 225px;
    width: 1.5px;
    height: 195px;
    background: var(--rule-grey);
  }
  .contact-list {
    position: absolute;
    left: 632px;
    top: 222px;
    margin: 0;
    padding: 0;
    list-style: none;
  }
  .contact-list li {
    display: flex;
    align-items: center;
    gap: 12px;
    font-size: 22px;
    color: var(--ink);
    height: 48px;
    white-space: nowrap;
  }
  .contact-list svg {
    width: 22px;
    height: 22px;
    fill: var(--navy);
    flex: none;
  }
  .services-rule {
    position: absolute;
    left: 70px;
    right: 70px;
    top: 520px;
    height: 1.5px;
    background: var(--rule-grey);
  }
  .services {
    position: absolute;
    left: 70px;
    right: 70px;
    top: 540px;
    margin: 0;
    font-size: 20px;
    font-style: italic;
    color: var(--text-grey);
    text-align: center;
    white-space: nowrap;
  }
</style>
</head>
<body>
<main class="canvas">
  <section class="business-card">
    <svg class="card-shading" viewBox="0 0 1000 647" aria-hidden="true">
      <polygon points="0,0 720,0 260,647 0,647" fill="var(--card-shade)"/>
      <polygon points="0,0 420,0 0,420" fill="var(--card-shade-deep)"/>
    </svg>

    <div class="brand">
      <span class="brand-mark"></span>
      <span class="brand-name">Talvane Property Services</span>
    </div>

    <div class="holder">
      <h1 class="holder-name">DEREK HOLLINGSBY</h1>
      <p class="holder-title">CEng, MSoHTF</p>
    </div>

    <div class="divider"></div>

    <ul class="contact-list">
      <li>
        <svg viewBox="0 0 24 24" aria-hidden="true"><path d="M6.6 10.8a15.1 15.1 0 0 0 6.6 6.6l2.2-2.2c.3-.3.7-.4 1-.2 1.1.4 2.3.6 3.6.6.6 0 1 .4 1 1V20c0 .6-.4 1-1 1A17 17 0 0 1 3 4c0-.6.4-1 1-1h3.5c.6 0 1 .4 1 1 0 1.3.2 2.5.6 3.6.1.3 0 .7-.2 1z"/></svg>
        <span>07921 458 302</span>
      </li>
      <li>
        <svg viewBox="0 0 24 24" aria-hidden="true"><path d="M2 5h20v14H2z"/><path d="M2 5l10 8 10-8" fill="none" stroke="#fff" stroke-width="1.6"/></svg>
        <span>info@talvaneps-example.com</span>
      </li>
      <li>
        <svg viewBox="0 0 24 24" aria-hidden="true"><path d="M12 2a10 10 0 1 0 0 20 10 10 0 0 0 0-20zm6.9 6h-3a15.6 15.6 0 0 0-1.4-3.6A8 8 0 0 1 18.9 8zM12 4c.8 1.2 1.5 2.5 1.9 4h-3.8c.4-1.5 1.1-2.8 1.9-4zM4.3 14a8.2 8.2 0 0 1 0-4h3.4a16.5 16.5 0 0 0 0 4zm.8 2h3a15.6 15.6 0 0 0 1.4 3.6A8 8 0 0 1 5.1 16zm3-8h-3a8 8 0 0 1 4.4-3.6C8.9 5.5 8.4 6.7 8.1 8zM12 20c-.8-1.2-1.5-2.5-1.9-4h3.8c-.4 1.5-1.1 2.8-1.9 4zm2.3-6H9.7a14.7 14.7 0 0 1 0-4h4.6a14.7 14.7 0 0 1 0 4zm.2 5.6c.6-1.1 1.1-2.3 1.4-3.6h3a8 8 0 0 1-4.4 3.6zm1.8-5.6a16.5 16.5 0 0 0 0-4h3.4a8.2 8.2 0 0 1 0 4z"/></svg>
        <span>www.talvaneps-example.com</span>
      </li>
      <li>
        <svg viewBox="0 0 24 24" aria-hidden="true"><path d="M12 3l10 9h-3v9h-5v-6h-4v6H5v-9H2z"/></svg>
        <span>Glenmorrow, Aberdeen</span>
      </li>
    </ul>

    <div class="services-rule"></div>
    <p class="services">Legionella Risk Assessment | Portable Appliance Testing | Energy Performance Certificate</p>
  </section>
</main>
</body>
</html>
```